Marlow Label design search/01

We need a label design for a new customers chemical products. The label is 275mm wide and 165mm high. The design will be simple with lots of space left for us to thermally print the information required on each label. This thermal print is black. From the top down 70mm the label will be white. The logo size will be about 50mm-55mm across and 40mm-45mm down. The logo position needs to be 1 of the following positions
a) Cetred at the bottom
b) Centred at the top
c) At the bottom no closer than 70mm to the right edge
The attached logo has 8 logos on it and we would like the Marlow Reagents on the left.
Requirements
Must have
- Logo
- look at attached info
Nice to have
- Simple and clean

```html
<!DOCTYPE html>
<html lang="en">
<head>
<meta charset="utf-8">
<title>Marlow Reagents – Label Concepts</title>
<link href="https://fonts.googleapis.com/css2?family=Titillium+Web:wght@700&display=swap" rel="stylesheet">
<style>
  :root {
    --brand-red: #b31b0b;
    --paper: #ffffff;
    --frame: #2a2a2a;
    --tint-loops: #f1d5d0;
    --tint-maze: #f4dedb;
    --tint-waves: #f8e8e6;
    --tint-molecules: #f3dad6;
  }
  * { margin: 0; padding: 0; box-sizing: border-box; }
  html, body {
    width: 1200px;
    height: 746px;
    overflow: hidden;
    background: var(--paper);
  }
  .sheet {
    position: relative;
    width: 1200px;
    height: 746px;
  }
  .label {
    position: absolute;
    width: 573px;
    height: 344px;
    border: 1px solid var(--frame);
    background: var(--paper);
    overflow: hidden;
  }
  .label--loops     { left: 19px;  top: 21px; }
  .label--maze      { left: 608px; top: 21px; }
  .label--waves     { left: 19px;  top: 382px; }
  .label--molecules { left: 608px; top: 382px; }

  .brand {
    position: absolute;
    top: 11px;
    left: 50%;
    width: 150px;
    height: 92px;
    margin-left: -75px;
    display: flex;
    align-items: center;
    justify-content: center;
    gap: 8px;
  }
  .brand__mark {
    width: 34px;
    height: 34px;
    background: var(--brand-red);
    flex: none;
  }
  .brand__name {
    font-family: "Titillium Web", sans-serif;
    font-weight: 700;
    font-size: 20px;
    line-height: 1.05;
    letter-spacing: 1px;
    color: var(--brand-red);
    text-transform: uppercase;
  }

  .pattern {
    position: absolute;
    left: 0;
    bottom: 0;
    width: 100%;
    height: 196px;
  }
  .label--loops .pattern {
    background: linear-gradient(to bottom, rgba(241, 213, 208, 0) 0%, var(--tint-loops) 40%, var(--tint-loops) 100%);
  }
  .label--maze .pattern {
    height: 192px;
    background: linear-gradient(to bottom, rgba(244, 222, 219, 0) 0%, var(--tint-maze) 30%, var(--tint-maze) 100%);
  }
  .label--waves .pattern {
    background: linear-gradient(to bottom, rgba(248, 232, 230, 0) 0%, var(--tint-waves) 60%, var(--tint-waves) 100%);
  }
  .label--molecules .pattern {
    height: 188px;
    background: linear-gradient(to bottom, rgba(243, 218, 214, 0) 0%, rgba(243, 218, 214, 0.6) 25%, var(--tint-molecules) 55%, var(--tint-molecules) 100%);
  }
</style>
</head>
<body>
<main class="sheet">
  <section class="label label--loops">
    <div class="brand"><span class="brand__mark"></span><span class="brand__name">Marlow<br>Reagents</span></div>
    <div class="pattern" role="img" aria-label="Pale red pattern of bold interlocking rounded loops fading in from the top"></div>
  </section>

  <section class="label label--maze">
    <div class="brand"><span class="brand__mark"></span><span class="brand__name">Marlow<br>Reagents</span></div>
    <div class="pattern" role="img" aria-label="Pale red maze-like pattern of dense meandering lines fading in from the top"></div>
  </section>

  <section class="label label--waves">
    <div class="brand"><span class="brand__mark"></span><span class="brand__name">Marlow<br>Reagents</span></div>
    <div class="pattern" role="img" aria-label="Fine pale red pattern of repeating wavy concentric lines fading in from the top"></div>
  </section>

  <section class="label label--molecules">
    <div class="brand"><span class="brand__mark"></span><span class="brand__name">Marlow<br>Reagents</span></div>
    <div class="pattern" role="img" aria-label="Pale red rows of linked droplet shapes resembling molecules, fading in from the top"></div>
  </section>
</main>
</body>
</html>
```